Just upload my Logo
Simple
Elsa Marroquín
quillmarshimages@postnook.net
Follow me in Chatterloom
* Wedding
* Engagment
* Maternity
* Newborn
* Family
* Events......etc

```html
<!DOCTYPE html>
<html lang="en">
<head>
<meta charset="utf-8">
<title>Quillmarsh Images – Business Cards</title>
<link rel="stylesheet" href="https://fonts.googleapis.com/css2?family=Arimo:wght@400;700&display=swap">
<style>
  :root{
    --bg:#e9e6e2;
    --pink:#e0218a;
    --ink:#1c1c1c;
    --muted:#555;
    --white-card-top:#ffffff;
    --white-card-bottom:#e6e6e6;
    --black-card-top:#3a3a3a;
    --black-card-mid:#0e0e0e;
    --light-text:#f2f2f2;
  }
  *{box-sizing:border-box;margin:0;padding:0}
  html,body{width:1200px;height:911px;overflow:hidden}
  body{background:var(--bg);font-family:"Arimo",Arial,sans-serif}
  .sheet{
    width:1200px;height:911px;
    display:grid;
    grid-template-columns:520px 520px;
    grid-template-rows:300px 300px;
    gap:60px 40px;
    justify-content:center;align-content:center;
  }
  .card{
    position:relative;border-radius:18px;overflow:hidden;
    box-shadow:0 6px 18px rgba(0,0,0,.25);
    display:flex;flex-direction:column;align-items:center;
  }
  .card--light{background:linear-gradient(var(--white-card-top),var(--white-card-bottom));color:var(--ink)}
  .card--dark{background:radial-gradient(ellipse at 50% 35%,var(--black-card-top),var(--black-card-mid) 70%);color:var(--light-text)}
  .brand{display:flex;align-items:center;gap:14px;margin-top:34px}
  .brand__art{width:96px;height:90px;border-radius:8px}
  .card--light .brand__art{background:linear-gradient(135deg,#8a8a8a,#cfcfcf)}
  .card--dark .brand__art{background:linear-gradient(135deg,#d9d9d9,#6e6e6e)}
  .brand__name{font-size:30px;font-weight:400;letter-spacing:.5px}
  .brand__sub{font-size:13px;letter-spacing:4px;text-transform:uppercase;color:var(--pink)}
  .rule{width:74%;height:2px;margin:14px 0 10px;background:linear-gradient(90deg,transparent,var(--pink),transparent)}
  .owner{font-size:17px;font-weight:700;margin-bottom:12px}
  .contact{font-size:12px;line-height:1.6;width:62%}
  .contact span{display:inline-block;width:46px}
  .follow{font-size:13px;font-weight:700;color:var(--pink);margin-bottom:6px}
  .services{list-style:none;display:grid;grid-template-columns:repeat(3,auto);gap:4px 18px;font-size:12px}
  .services li{display:flex;align-items:center;gap:5px}
  .services svg{width:9px;height:9px}
</style>
</head>
<body>
<main class="sheet">

  <article class="card card--light">
    <div class="brand">
      <div class="brand__art" role="img" aria-label="Illustrated bird perched on a floral branch"></div>
      <div>
        <div class="brand__name">Quillmarsh</div>
        <div class="brand__sub">Images</div>
      </div>
    </div>
    <div class="rule"></div>
    <div class="owner">Elsa Marroquín</div>
    <div class="contact">
      <div><span>Cell:</span>(555) 014-2283</div>
      <div><span>Email:</span>quillmarshimages@postnook.net</div>
    </div>
  </article>

  <article class="card card--dark">
    <div class="brand">
      <div class="brand__art" role="img" aria-label="Illustrated bird perched on a floral branch"></div>
      <div>
        <div class="brand__name">Quillmarsh</div>
        <div class="brand__sub">Images</div>
      </div>
    </div>
    <div class="rule"></div>
    <div class="owner">Elsa Marroquín</div>
    <div class="contact">
      <div><span>Cell:</span>(555) 014-2283</div>
      <div><span>Email:</span>quillmarshimages@postnook.net</div>
    </div>
  </article>

  <article class="card card--light">
    <div class="brand">
      <div class="brand__art" role="img" aria-label="Illustrated bird perched on a floral branch"></div>
      <div class="brand__name">Quillmarsh</div>
    </div>
    <div class="rule"></div>
    <div class="follow">Follow me in Chatterloom</div>
    <ul class="services">
      <li><svg viewBox="0 0 10 10"><circle cx="5" cy="5" r="4" fill="#e0218a"/></svg>Wedding</li>
      <li><svg viewBox="0 0 10 10"><circle cx="5" cy="5" r="4" fill="#e0218a"/></svg>Engagement</li>
      <li><svg viewBox="0 0 10 10"><circle cx="5" cy="5" r="4" fill="#e0218a"/></svg>Maternity</li>
      <li><svg viewBox="0 0 10 10"><circle cx="5" cy="5" r="4" fill="#e0218a"/></svg>Newborn</li>
      <li><svg viewBox="0 0 10 10"><circle cx="5" cy="5" r="4" fill="#e0218a"/></svg>Family</li>
      <li><svg viewBox="0 0 10 10"><circle cx="5" cy="5" r="4" fill="#e0218a"/></svg>Events……etc</li>
    </ul>
  </article>

  <article class="card card--dark">
    <div class="brand">
      <div class="brand__art" role="img" aria-label="Illustrated bird perched on a floral branch"></div>
      <div class="brand__name">Quillmarsh</div>
    </div>
    <div class="rule"></div>
    <div class="follow">Follow me in Chatterloom</div>
    <ul class="services">
      <li><svg viewBox="0 0 10 10"><circle cx="5" cy="5" r="4" fill="#e0218a"/></svg>Wedding</li>
      <li><svg viewBox="0 0 10 10"><circle cx="5" cy="5" r="4" fill="#e0218a"/></svg>Engagement</li>
      <li><svg viewBox="0 0 10 10"><circle cx="5" cy="5" r="4" fill="#e0218a"/></svg>Maternity</li>
      <li><svg viewBox="0 0 10 10"><circle cx="5" cy="5" r="4" fill="#e0218a"/></svg>Newborn</li>
      <li><svg viewBox="0 0 10 10"><circle cx="5" cy="5" r="4" fill="#e0218a"/></svg>Family</li>
      <li><svg viewBox="0 0 10 10"><circle cx="5" cy="5" r="4" fill="#e0218a"/></svg>Events……etc</li>
    </ul>
  </article>

</main>
</body>
</html>
```